Offshore Energy Projects Management Consultancy needs a business card design

Logo available. We provide teams to deliver engineering consultancy, project management and delivery teams mainly in the offshore renewables sector. The company is all about bringing the right people to a project to deliver the scope.

The business card will be used for all staff.

The business card should be quite simple, vibrant and uncluttered but convey experience, enthusiasm and integration.

Target Market(s)

Energy Project Developers and Tier 1 construction companies

Contact Information for Business Card

Logo should be on the back of the card. I'm happy for the designer to play with the colour of the logo and background colour.

Front of the card should convey all the must have information in a clear and professional manner but without being overly traditional.

Colors

Designer to choose colors to be used in the design.

Requirements
Must have
• Land Line Tel Number, Mobile Tel Number, Email, business address, web address.

```html
<!DOCTYPE html>
<html lang="en">
<head>
<meta charset="utf-8">
<title>Tidewell Project Partners – Business Card</title>
<link rel="stylesheet" href="https://fonts.googleapis.com/css2?family=Arimo:wght@400;700&display=swap">
<style>
  :root {
    --page-bg: #eeeeee;
    --card-bg: #ffffff;
    --ink-grey: #6d6e71;
    --brand-blue: #1f73b7;
    --brand-sky: #3aaee3;
    --photo-light: #f3f3f3;
    --photo-mid: #d6d6d6;
    --photo-dark: #a9a9a9;
  }
  * { box-sizing: border-box; margin: 0; padding: 0; }
  html, body {
    width: 1200px; height: 864px; overflow: hidden;
    background: var(--page-bg);
    font-family: "Arimo", Helvetica, Arial, sans-serif;
  }
  .canvas { position: relative; width: 1200px; height: 864px; }
  .card {
    position: absolute; top: 264px;
    width: 520px; height: 336px;
    background: var(--card-bg);
    box-shadow: 0 10px 30px rgba(0,0,0,0.12);
    overflow: hidden;
  }
  .card--front { left: 60px; }
  .card--back { left: 620px; }

  /* Front */
  .address {
    position: absolute; left: 40px; top: 30px;
    font-size: 15px; line-height: 1.3; color: var(--ink-grey);
  }
  .person { position: absolute; left: 40px; top: 112px; }
  .person__name { font-size: 20px; color: var(--ink-grey); }
  .person__title { font-size: 15px; font-weight: 700; color: var(--brand-blue); margin-top: 2px; }
  .web {
    position: absolute; left: 40px; top: 214px;
    font-size: 15px; font-weight: 700; color: var(--brand-blue);
  }
  .contacts {
    position: absolute; left: 300px; top: 120px;
    font-size: 13.5px; line-height: 1.4; color: var(--ink-grey);
    list-style: none;
  }
  .contacts__label { font-weight: 700; color: var(--brand-blue); display: inline-block; width: 20px; }
  .brand-mark {
    position: absolute; right: 36px; bottom: 34px;
    display: flex; align-items: center; gap: 8px;
    font-size: 16px; font-weight: 700; color: var(--brand-blue);
  }
  .brand-mark__dot {
    width: 14px; height: 14px; border-radius: 50%; background: var(--brand-sky);
  }

  /* Back */
  .back-photo {
    position: absolute; inset: 0;
    background: radial-gradient(ellipse at 45% 20%, var(--photo-dark) 0%, var(--photo-mid) 40%, var(--photo-light) 80%);
  }
  .back-brand {
    position: absolute; left: 0; right: 0; top: 128px;
    text-align: center;
    font-size: 30px; font-weight: 700; color: var(--brand-blue);
    letter-spacing: 0.5px;
  }
  .socials {
    position: absolute; left: 0; right: 0; top: 196px;
    display: flex; justify-content: center; gap: 26px;
    list-style: none;
    font-size: 13px; color: var(--ink-grey);
  }
  .socials__item { display: flex; align-items: center; gap: 6px; }
  .socials__dot { width: 12px; height: 12px; border-radius: 50%; background: var(--brand-blue); }
</style>
</head>
<body>
<main class="canvas">
  <section class="card card--front" aria-label="Card front">
    <address class="address">
      The Harbourline Building,<br>
      212 Quay Road,<br>
      Northport, NP4 2LX
    </address>
    <div class="person">
      <p class="person__name">Name Surname</p>
      <p class="person__title">Job Title</p>
    </div>
    <p class="web">tpp.ltd</p>
    <ul class="contacts">
      <li><span class="contacts__label">T:</span> +44(0) 1632 960 418</li>
      <li><span class="contacts__label">M:</span> +44(0) 7700 900 246</li>
      <li><span class="contacts__label">E:</span> name.surname@tpp.ltd</li>
    </ul>
    <div class="brand-mark">
      <span class="brand-mark__dot"></span>
      <span>Tidewell Project Partners</span>
    </div>
  </section>

  <section class="card card--back" aria-label="Card back">
    <div class="back-photo" role="img" aria-label="Greyscale photograph of a hand working over engineering plan drawings"></div>
    <p class="back-brand">Tidewell Project Partners</p>
    <ul class="socials">
      <li class="socials__item"><span class="socials__dot"></span>@TPPlimited</li>
      <li class="socials__item"><span class="socials__dot"></span>/TPP.ltd</li>
      <li class="socials__item"><span class="socials__dot"></span>company/tppltd</li>
    </ul>
  </section>
</main>
</body>
</html>
```